Varnek Modellwerk GmbH needed a letterhead template

For English scroll down. We need a letterhead template and since we already have our logo design successfully with you, we now want to also design the letterhead with you. Down in the uploaded file you see what is important and what should definitely be seen on our template. The template should be like the homepage (www.modellwerk-varnek.example) held in red, blue and white. We need a letter-head submission. In the bottom in the chapter "databases uploading" you can find the most important things, did must be on the submission. The submission shoulderstand be in the colors blue, red and white like our homepage (www.modellwerk-varnek.example).

```html
<!DOCTYPE html>
<html lang="de">
<head>
<meta charset="utf-8">
<title>Varnek Modellwerk GmbH – Briefpapier</title>
<link rel="stylesheet" href="https://fonts.googleapis.com/css2?family=PT+Sans:wght@400;700&display=swap">
<style>
  :root {
    --brand-blue: #1a6bb4;
    --brand-red: #c8202f;
    --paper: #ffffff;
    --page-edge: #bdbdbd;
    --canvas: #ffffff;
    --watermark: #f3f6fa;
  }
  * { margin: 0; padding: 0; box-sizing: border-box; }
  html, body {
    width: 1200px; height: 1000px; overflow: hidden;
    background: var(--canvas);
    font-family: "PT Sans", sans-serif;
  }
  .letterhead {
    position: absolute; left: 268px; top: 31px;
    width: 663px; height: 938px;
    background: var(--paper);
    border: 1px solid var(--page-edge);
    border-bottom: none;
  }
  .brand {
    position: absolute; left: 30px; top: 46px;
    display: flex; align-items: center; gap: 10px;
  }
  .brand-dot {
    width: 22px; height: 22px; border-radius: 50%;
    background: var(--brand-red);
  }
  .brand-name {
    font-weight: 700; font-size: 26px; color: var(--brand-blue);
    letter-spacing: -0.2px;
  }
  .sender {
    position: absolute; left: 490px; top: 41px;
    font-weight: 700; font-size: 12px; line-height: 14.6px;
    color: var(--brand-blue); font-style: normal;
  }
  .watermark {
    position: absolute; left: 182px; top: 356px;
    width: 306px; height: 222px; border-radius: 50%;
    background: radial-gradient(ellipse at center, var(--watermark) 0%, rgba(243,246,250,0) 70%);
  }
  .rule-red {
    position: absolute; left: 0; right: 0; top: 860px;
    height: 3px; background: var(--brand-red);
  }
  .footer {
    position: absolute; left: 0; right: 0; top: 867px; bottom: 0;
    background: var(--brand-blue); color: #fff;
    font-weight: 700; font-size: 11px; line-height: 13.5px;
  }
  .footer-col { position: absolute; top: 9px; white-space: nowrap; }
  .footer-col.company { left: 14px; }
  .footer-col.contact { left: 256px; }
  .footer-col.bank { left: 488px; }
  .footer-line { display: flex; align-items: center; }
  .footer-line .icon { width: 11px; height: 11px; flex: none; }
  .indent { padding-left: 11px; }
  .contact .footer-line .icon { margin-right: 2px; }
</style>
</head>
<body>
  <main class="letterhead">
    <div class="brand">
      <span class="brand-dot"></span>
      <span class="brand-name">Modellwerk Varnek</span>
    </div>

    <address class="sender">
      Varnek Modellwerk GmbH<br>
      Lindenweg 12<br>
      6020 Aldrach, Tirol<br>
      Österreich
    </address>

    <div class="watermark" role="img" aria-label="Faint brand watermark in soft red and blue tones"></div>

    <div class="rule-red"></div>

    <footer class="footer">
      <div class="footer-col company">
        <div class="footer-line">
          <svg class="icon" viewBox="0 0 12 12"><path d="M6 1.5a2.6 2.6 0 0 0-2.6 2.6C3.4 6 6 9 6 9s2.6-3 2.6-4.9A2.6 2.6 0 0 0 6 1.5zm0 3.6a1 1 0 1 1 0-2 1 1 0 0 1 0 2z" fill="#fff"/></svg>
          <span>Geschäftsführer Dr. Halvorsen Lukas</span>
        </div>
        <div class="indent">Lindenweg 12</div>
        <div class="indent">6020 Aldrach, Tirol</div>
        <div class="indent">Österreich</div>
      </div>

      <div class="footer-col contact">
        <div class="footer-line">
          <svg class="icon" viewBox="0 0 12 12"><path d="M4 2.5 5.2 4.6 4.4 5.4a5 5 0 0 0 2.2 2.2l.8-.8 2.1 1.2-.6 1.2C6 9.3 2.7 6 2.8 3.1z" fill="#fff"/></svg>
          <span>Telefon: 0800 XX XX XX</span>
        </div>
        <div class="footer-line">
          <svg class="icon" viewBox="0 0 12 12"><rect x="3" y="4" width="6" height="4.2" rx="0.6" fill="#fff"/><path d="M3.2 4.3 6 6.4l2.8-2.1" stroke="#1a6bb4" stroke-width="0.7" fill="none"/></svg>
          <span>Mail: contact@modellwerk-varnek.example</span>
        </div>
        <div class="footer-line">
          <svg class="icon" viewBox="0 0 12 12"><circle cx="6" cy="6" r="2.8" fill="none" stroke="#fff" stroke-width="0.9"/><path d="M3.2 6h5.6M6 3.2c1.4 1.6 1.4 4 0 5.6M6 3.2c-1.4 1.6-1.4 4 0 5.6" stroke="#fff" stroke-width="0.6" fill="none"/></svg>
          <span>Web: www.modellwerk-varnek.example</span>
        </div>
      </div>

      <div class="footer-col bank">
        <div>Firnbach Bank XXXX</div>
        <div>IBAN: ATXX XXXX XXXX XXXX</div>
        <div>BIC: XXXX</div>
        <div>UID - Nr .: ATUXXXXX</div>
      </div>
    </footer>
  </main>
</body>
</html>
```